Business Card Design Project

I require a business card design that looks professional for a small building company. Holloway Builders is the name of the company and i don't want to use a house or building design for a logo. I require a logo design for the card incorporating the name Holloway Builders but designed smartly.

We are a Registered Building Practitioner so the small logo attached must also be used on the card.

We cover a large range of Building / Construction, Concrete, Steelwork. Not sure how to implement this.

Colors are flexible, maybe a dark grey background with white writting over it, but i am keen to see other options.

Thanks.

Target Market(s)

Anyone

Industry/Entity Type

Building

Requirements
Must have
• The logo attached must be incorporated - can be small
A logo for my company needs to be included - using Holloway Builders as the base with no picture of a house or buildings.

```html
<!DOCTYPE html>
<html lang="en">
<head>
<meta charset="utf-8">
<title>Holloway Builders – Business Card</title>
<link rel="stylesheet" href="https://fonts.googleapis.com/css2?family=Exo+2:wght@400;500;800&display=swap">
<style>
  :root {
    --bg: #2a2b2d;
    --teal: #0b7479;
    --teal-card: #0f8087;
    --ink: #1f2224;
    --paper: #f7f7f7;
    --text-dark: #2b2b2b;
  }
  * { margin: 0; padding: 0; box-sizing: border-box; }
  html, body { width: 1200px; height: 900px; overflow: hidden; }
  body {
    background: var(--bg);
    font-family: "Exo 2", sans-serif;
    position: relative;
  }
  .card {
    position: absolute;
    width: 520px;
    height: 300px;
    box-shadow: 0 14px 30px rgba(0,0,0,.45);
    overflow: hidden;
  }
  /* Front */
  .card--front { left: 130px; top: 100px; background: var(--paper); }
  .front__logo {
    position: absolute; right: 34px; top: 30px;
    font-weight: 800; font-size: 34px; line-height: .95;
    color: var(--teal); text-transform: uppercase; letter-spacing: 1px;
  }
  .front__name-band {
    position: absolute; left: 0; top: 102px; width: 270px; height: 32px;
    background: var(--teal); color: #fff;
    font-size: 19px; font-weight: 500; letter-spacing: 1px;
    text-transform: uppercase; padding-left: 36px; line-height: 32px;
  }
  .front__details {
    position: absolute; left: 36px; top: 142px;
    font-size: 11px; color: var(--text-dark); text-transform: uppercase;
    letter-spacing: .4px; line-height: 1.55;
  }
  .front__details .role { margin-bottom: 8px; }
  .front__details .gap { margin-top: 8px; }
  .label { color: var(--teal); font-weight: 500; }
  .front__web { color: var(--teal); font-size: 12.5px; letter-spacing: 2px; }
  .front__badge {
    position: absolute; left: 36px; top: 262px;
    width: 64px; height: 18px; background: var(--teal); border-radius: 2px;
  }
  /* Back */
  .card--back { left: 550px; top: 480px; background: var(--teal-card); }
  .back__logo {
    position: absolute; left: 0; right: 0; top: 58px; text-align: center;
    font-weight: 800; font-size: 52px; line-height: .92;
    color: var(--ink); text-transform: uppercase; letter-spacing: 1px;
  }
  .back__band {
    position: absolute; left: 0; right: 0; top: 176px; height: 28px;
    background: var(--ink); color: var(--teal-card);
    font-size: 15px; letter-spacing: 1.5px; text-align: center; line-height: 28px;
  }
  .back__web {
    position: absolute; left: 0; right: 0; top: 222px; text-align: center;
    font-size: 15px; font-weight: 500; letter-spacing: 3px; color: var(--ink);
  }
</style>
</head>
<body>
  <section class="card card--front">
    <div class="front__logo">Holloway<br>Builders</div>
    <div class="front__name-band">Marlene Castor</div>
    <div class="front__details">
      <p class="role">Licensed Plumber</p>
      <p>Address 48 Kestrel Lane, Brookfield CA 90412</p>
      <p class="gap"><span class="label">P:</span> 555 0192 374 &nbsp;<span class="label">F:</span> 555 0192 375</p>
      <p><span class="label">E:</span> marlene@hollowaybuilders.com</p>
      <p class="front__web">www.hollowaybuilders.com</p>
    </div>
    <div class="front__badge" role="img" aria-label="Registered building practitioner badge"></div>
  </section>

  <section class="card card--back">
    <div class="back__logo">Holloway<br>Builders</div>
    <div class="back__band">Building &nbsp;|&nbsp; Construction &nbsp;|&nbsp; Concrete &nbsp;|&nbsp; Steelwork</div>
    <div class="back__web">WWW.HOLLOWAYBUILDERS.COM</div>
  </section>
</body>
</html>
```